Soap box for artisan soaps, eco-look, high design

We need a soap box for our lovely artisan soaps. The box size is: 9 cm height x 6,5 cm width x 2,8 cm depth. It would be nice when there is a small window in the box so you can see the soap.

See attachment for an example soap box (upside down). Please use the same elements such as texts and industrie logos. The idea is that we have a generic design that we can custom-made for different soaps. We have 15 different soaps in total at the moment.

Target Market(s)

Middle to high income

Font styles to use
Decorative
Script

Requirements
Must have
• Dutch text:
• Etherische oliën
• Handgemaakt
• Natuurlijke ingrediënten

```html
<!DOCTYPE html>
<html lang="nl">
<head>
<meta charset="utf-8">
<title>Maelle – Etherische zeep</title>
<link rel="stylesheet" href="https://fonts.googleapis.com/css2?family=Playfair+Display:wght@700&family=Allura&family=Arimo:wght@400;700&display=swap">
<style>
  :root {
    --bg: #ffffff;
    --kraft: #b08d68;
    --kraft-side: #a3805c;
    --kraft-lower: #a8845f;
    --brand: #163a5c;
    --ink: #2a2118;
    --label-white: #f6efe6;
    --lemon: #d8c24a;
    --orange: #e39a4e;
    --lavender: #c18fb4;
  }
  * { margin: 0; padding: 0; box-sizing: border-box; }
  html, body { width: 1200px; height: 857px; overflow: hidden; background: var(--bg); }
  .canvas { position: relative; width: 1200px; height: 857px; }

  .box { position: absolute; top: 290px; height: 325px; display: flex; }
  .box--lemon { left: 232px; --accent: var(--lemon); }
  .box--orange { left: 495px; --accent: var(--orange); }
  .box--lavender { left: 760px; --accent: var(--lavender); }

  .box__side {
    position: relative; width: 44px; height: 100%;
    background: var(--kraft-side); overflow: hidden;
  }
  .box__side::after {
    content: ""; position: absolute; left: 0; right: 0; top: 180px; height: 4px;
    background: var(--accent);
  }
  .ingredients {
    position: absolute; top: 8px; left: 40px;
    width: 165px; transform: rotate(90deg); transform-origin: top left;
    font: 400 6.4px/1.35 "Arimo", sans-serif; color: var(--ink); text-align: justify;
  }
  .ingredients b { font-weight: 700; }

  .box__front {
    position: relative; width: 172px; height: 100%;
    background: var(--kraft); overflow: hidden; text-align: center;
  }
  .box__lower {
    position: absolute; left: 0; right: 0; top: 184px; bottom: 0;
    background: var(--kraft-lower);
  }
  .box__band {
    position: absolute; left: 0; right: 0; top: 180px; height: 4px; background: var(--accent);
  }
  .brand {
    position: absolute; top: 22px; left: 0; right: 0;
    font: 700 25px/1 "Playfair Display", serif; color: var(--brand);
  }
  .scent {
    position: absolute; top: 66px; left: 0; right: 0;
    font: 400 25px/1 "Allura", cursive; color: var(--ink);
    transform: rotate(6deg);
  }
  .type {
    position: absolute; top: 104px; left: 0; right: 0;
    font: 400 11px/1 "Arimo", sans-serif; color: var(--ink); letter-spacing: 0.2px;
  }
  .window { position: absolute; top: 128px; left: 28px; width: 116px; height: 110px; }
  .claims {
    position: absolute; top: 258px; left: 0; right: 0;
    font: 400 11px/18px "Arimo", sans-serif; color: var(--label-white);
  }
</style>
</head>
<body>
<main class="canvas">

  <article class="box box--lemon">
    <div class="box__side"><p class="ingredients"><b>Ingrediënten:</b> olijfolie, kokosolie, palmolie, water, natriumhydroxide, etherische olie, klei, zaden, plantaardige glycerine, citral, limonene, linalool.</p></div>
    <div class="box__front">
      <div class="box__lower"></div>
      <div class="box__band"></div>
      <h2 class="brand">Maelle</h2>
      <p class="scent">Lemon and Poppy</p>
      <p class="type">ETHERISCHE ZEEP</p>
      <svg class="window" viewBox="0 0 100 90" role="img" aria-label="Venster met zicht op gele citroen-maanzaadzeep">
        <defs><linearGradient id="soap-lemon" x1="0" x2="1"><stop offset="0" stop-color="#d89a3a"/><stop offset="0.6" stop-color="#c9893a"/><stop offset="1" stop-color="#b8a49a"/></linearGradient></defs>
        <path d="M50 88 C20 62 2 46 2 24 C2 10 13 2 26 2 C38 2 46 9 50 18 C54 9 62 2 74 2 C87 2 98 10 98 24 C98 46 80 62 50 88 Z" fill="url(#soap-lemon)"/>
      </svg>
      <p class="claims">Etherische oliën<br>Handgemaakt<br>Natuurlijke ingrediënten</p>
    </div>
  </article>

  <article class="box box--orange">
    <div class="box__side"><p class="ingredients"><b>Ingrediënten:</b> olijfolie, kokosolie, palmolie, water, natriumhydroxide, etherische olie, klei, zaden, plantaardige glycerine, citral, limonene, linalool.</p></div>
    <div class="box__front">
      <div class="box__lower"></div>
      <div class="box__band"></div>
      <h2 class="brand">Maelle</h2>
      <p class="scent">Orange Sweet</p>
      <p class="type">ETHERISCHE ZEEP</p>
      <svg class="window" viewBox="0 0 100 90" role="img" aria-label="Venster met zicht op oranje gemarmerde zeep">
        <defs><linearGradient id="soap-orange" x1="0" x2="1" y1="0" y2="1"><stop offset="0" stop-color="#f1d2c0"/><stop offset="0.5" stop-color="#e6a084"/><stop offset="1" stop-color="#f0dccd"/></linearGradient></defs>
        <path d="M50 88 C20 62 2 46 2 24 C2 10 13 2 26 2 C38 2 46 9 50 18 C54 9 62 2 74 2 C87 2 98 10 98 24 C98 46 80 62 50 88 Z" fill="url(#soap-orange)"/>
      </svg>
      <p class="claims">Etherische oliën<br>Handgemaakt<br>Natuurlijke ingrediënten</p>
    </div>
  </article>

  <article class="box box--lavender">
    <div class="box__side"><p class="ingredients"><b>Ingrediënten:</b> olijfolie, kokosolie, palmolie, water, natriumhydroxide, etherische olie, klei, zaden, plantaardige glycerine, citral, limonene, linalool.</p></div>
    <div class="box__front">
      <div class="box__lower"></div>
      <div class="box__band"></div>
      <h2 class="brand">Maelle</h2>
      <p class="scent">Lavender</p>
      <p class="type">ETHERISCHE ZEEP</p>
      <svg class="window" viewBox="0 0 100 90" role="img" aria-label="Venster met zicht op paars-witte lavendelzeep">
        <defs><linearGradient id="soap-lavender" x1="0" x2="1" y1="0" y2="1"><stop offset="0" stop-color="#e8ddd6"/><stop offset="0.55" stop-color="#a58ad0"/><stop offset="1" stop-color="#6b55a8"/></linearGradient></defs>
        <path d="M50 88 C20 62 2 46 2 24 C2 10 13 2 26 2 C38 2 46 9 50 18 C54 9 62 2 74 2 C87 2 98 10 98 24 C98 46 80 62 50 88 Z" fill="url(#soap-lavender)"/>
      </svg>
      <p class="claims">Etherische oliën<br>Handgemaakt<br>Natuurlijke ingrediënten</p>
    </div>
  </article>

</main>
</body>
</html>
```